Come crowdsource a Web Design for a brazilian crowdsource Startup!

> NAME OF OUR STARTUP:
Mundaleo

> DESCRIPTION OF OUR STARTUP:
We are a crowdsourcing startup in Brazil providing consultancy and technology to support other companies to crowdsource their projects.
We also operate doing big crowdsource campaings related to polemic subjects in Brazil.

> WHAT ARE OUR TARGET AUDIENCE?
Our target audience are young people around 20-35 years old.
Generation Y (Millennial Generation)

> WHAT IS OUR INDUSTRY?
Internet, web

> WHAT DO WE NEED?
We need a Web Design for our first site.

We need 5 pages:
- Home
- What is Crowdsourcing?
- Solutions
- About Us
- Blog
- A box for the "Contact" tab (this is not a page)

Please, find attached a Layout Sketch of what I've imagined.

Lets talk about the sketch:
Well, first of all, it's a SKETCH, so you don't have to send proposals exactly as the sketch. The sketch is just to show how I've imagined the ditribution of the content boxes. For example, the menu bar doesnt need to be a rectangle exactly like the sketch, but, I would like to have the menu on the right side of the logo. Also, you will see that the boxes are all squeezed, of course I dont want them soo squeezed! Again, its juust a SKETCH!

About the images on the sketch:
IMG1 - Some nice and simple image related to collectivity or related to crowdsourcing or maybe use our O logo.

IMG2 - Some simple and creative image related to Consultancy. It doesnt need to be so obvious.

IMG3 - Some simple and creative image related to Web 2.0 Software Technology. It doesnt need to be so obvious.

IMG4 - Some simple and creative image related to a full package of Consultancy + Technology. It doesnt need to be so obvious.

IMG5 - Some nice and simple image related to collectivity or related to crowdsourcing.

IMG6 - Some nice and simple image related to Ideation. Maybe a light bulb? I dont know, be creative!

IMG7 - Some nice and simple image related to Crowdlabor. I dont know, be creative!

IMG8 - Some nice and simple image related to CrowdFeedback. Maybe a megaphone? A loudspeaker? I dont know, be creative!

IMG9 - Some nice and simple image related to us! Maybe our O logo ? I dont know, be creative!

THE CONTACT SIDE BAR - we need a nice and simple contact side bar. By the way, on the sketch this bar is shown only at the homepage, but when the site becomes real this bar will stay along all the pages.

THE CONTACT BOX - we need a nice and simple contact box.

ABOUT THE COLORS TO USE: we would like some color to our background and titles. We like colors similars to our logo: really light blue ? light green/blue ? light grey ? light orange ? I dont know, you guys knows more about that then me =)

CHATTERBOX SHARE/LIKE BUTTON: We would like a chatterbox share/like button somewhere on the site!

ABOUT THE ATTACHED FILES:

ADDITIONALS:
> The name Mundaleo comes from "collectivity". With our name we want to pass the idea of the collectivity from the crowdsource work model.

> Our communication is directed to the Generation Y.

> Remember, we are a Startup! So we need a modern and simple site, something like the web 2.0 trends. It must be beautiful =)

> We arent a serious company. We are a young and fun company! Please, dont come with old fashionable company sites.

> Be creative =] !

Target Market(s)

Our target audience are young people around 20-35 years old. Generation Y (Millennial Generation)

Industry/Entity Type

Communication

Requirements
Must have
• We need a Web Design for our first site.

We need 5 pages:
- Home
- What is Crowdsourcing?
- Solutions
- About Us
- Blog

ABOUT THE COLORS TO USE: we would like some color to our background and titles. We like colors similars to our logo: really light blue ? light green/blue ? light grey ? light oranges ? I dont know, you guys knows more about that then me =)

Should not have
• Poor/serious/old fashionable designs

```html
<!DOCTYPE html>
<html lang="en">
<head>
<meta charset="utf-8">
<title>Mundaleo – What is Crowdsourcing?</title>
<link rel="stylesheet" href="https://fonts.googleapis.com/css2?family=Molengo&family=Sintony:wght@400;700&family=Cuprum:ital@1&family=Varela+Round&display=swap">
<style>
:root{
  --ink:#1d1f26;
  --text:#2b2d33;
  --teal:#1a9aa8;
  --teal-dark:#13808d;
  --orange:#f7a237;
  --orange-deep:#f08a1e;
  --line:#cfd3d6;
  --header-top:#f1f5f8;
  --header-band:#dce8ee;
  --white:#ffffff;
}
*{margin:0;padding:0;box-sizing:border-box}
html,body{width:1200px;height:1135px;overflow:hidden;background:var(--white)}
body{position:relative;font-family:"Sintony",sans-serif;color:var(--text)}
.abs{position:absolute}

.site-header{left:0;top:0;width:1200px;height:134px;
  background:linear-gradient(180deg,var(--header-top) 0%,#eef3f6 66%,var(--header-band) 67%,#c9dbe4 88%,#e9eff2 100%)}
.brand{left:150px;top:26px;display:flex;align-items:center;gap:10px}
.brand-dot{width:46px;height:46px;border-radius:50%;background:var(--teal)}
.brand-name{font-family:"Varela Round",sans-serif;font-size:44px;color:var(--teal);line-height:1}
.main-nav{top:34px;left:0;width:1200px;height:26px}
.main-nav a{position:absolute;top:0;height:26px;line-height:26px;font-family:"Varela Round",sans-serif;font-size:13px;color:var(--ink);text-decoration:none;white-space:nowrap}
.main-nav a.active{width:210px;text-align:center;background:var(--orange);color:var(--white);border-radius:4px}

.hero-visual{left:142px;top:185px;width:360px;height:208px;border:4px solid var(--white);
  box-shadow:0 0 0 1px #d5d8da,0 2px 4px rgba(0,0,0,.15);
  background:radial-gradient(ellipse at 50% 55%,#ffffff 0%,#e6eef3 60%,#c8d7e0 100%)}
.page-title{left:539px;top:178px;font-family:"Molengo",sans-serif;font-size:31px;color:var(--ink);font-weight:400;white-space:nowrap}
.intro{left:539px;top:224px;width:505px;font-size:14.4px;line-height:23.5px}
.intro strong{color:var(--ink)}

.uses-ribbon{left:421px;top:480px;width:358px;height:38px}
.uses-ribbon span{position:absolute;left:0;top:0;width:100%;text-align:center;line-height:38px;font-family:"Molengo",sans-serif;font-size:22px;color:var(--white);white-space:nowrap}

.use-card{top:544px;width:270px}
.use-photo{height:156px;border:4px solid var(--white);box-shadow:0 0 0 1px #d5d8da,0 2px 4px rgba(0,0,0,.15)}
.use-title{margin-top:38px;text-align:center;font-family:"Molengo",sans-serif;font-size:22px;color:var(--teal);font-weight:400}
.use-text{margin-top:14px;text-align:center;font-family:Arial,Helvetica,sans-serif;font-size:12.6px;line-height:21.6px;color:var(--ink)}
.use-text b{font-weight:700}
.learn-more{display:block;width:80px;height:23px;margin:20px auto 0;background:var(--teal);border-radius:2px;color:var(--white);font-family:Arial,Helvetica,sans-serif;font-size:10px;font-weight:700;line-height:23px;text-align:center;text-decoration:none}

.contact-tab{left:0;top:403px;width:40px;height:141px;background:linear-gradient(90deg,#1e1e1e,#3b3b3b);border-radius:0 5px 5px 0;border:1px solid #555;border-left:none}
.contact-tab span{position:absolute;left:50%;top:50%;transform:translate(-50%,-50%) rotate(-90deg);font-family:"Varela Round",sans-serif;font-size:19px;letter-spacing:1px;color:var(--white)}

.footer-rule{left:0;top:1003px;width:1200px;height:3px;background:linear-gradient(90deg,#fbc790 0%,var(--orange-deep) 15%,var(--orange-deep) 85%,#fbc790 100%)}
.footer-band{left:0;top:1078px;width:1200px;height:8px;background:var(--orange-deep)}
.footer-italic{font-family:"Cuprum",sans-serif;font-style:italic;color:#444;white-space:nowrap}
.response-title{left:142px;top:1022px;font-size:18px}
.response-phones{left:142px;top:1046px;font-family:Arial,sans-serif;font-size:12px;color:var(--orange-deep)}
.footer-sep{top:1024px;width:2px;height:36px;background:#9a9a9a}
.footer-link{top:1030px;font-size:17px}
.newsletter-label{left:841px;top:1021px;font-size:16px}
.newsletter-field{left:844px;top:1042px;width:216px;height:20px;background:linear-gradient(180deg,#cfd1d3,#eceeef);border:1px solid #c3c5c7}
.newsletter-go{position:absolute;right:2px;top:2px;width:14px;height:14px;background:var(--orange-deep)}
.copyright{left:141px;top:1102px;font-size:11.5px;color:#333}
.like-box{left:908px;top:1098px;display:flex;align-items:center;gap:6px;font-family:Arial,sans-serif;font-size:9.5px;color:#333}
.like-btn{height:20px;padding:0 6px;border:1px solid #aab3c5;background:#eef1f6;border-radius:2px;line-height:18px;font-size:10px;font-weight:700;color:#3b5998}
.like-square{width:11px;height:11px;background:#4a67a7}
</style>
</head>
<body>

<header class="site-header abs">
  <div class="brand abs"><span class="brand-dot"></span><span class="brand-name">Mundaleo</span></div>
  <nav class="main-nav abs">
    <a href="#" style="left:529px">HOME</a>
    <a href="#" class="active" style="left:582px">WHAT IS CROWDSOURCING?</a>
    <a href="#" style="left:808px">SOLUTIONS</a>
    <a href="#" style="left:912px">ABOUT US</a>
    <a href="#" style="left:1007px">BLOG</a>
  </nav>
</header>

<div class="contact-tab abs"><span>CONTACT</span></div>

<main>
  <div class="hero-visual abs" role="img" aria-label="Business people standing on colourful puzzle pieces, symbolising collective work"></div>
  <h1 class="page-title abs">But, what is Crowdsourcing?</h1>
  <p class="intro abs"><strong>Crowdsourcing</strong> is the practice of obtaining needed services, ideas, or content by soliciting contributions from a large group of people, and especially from an online community, rather than from traditional employees or suppliers. Often used to subdivide tedious work or to fund-raise startup companies and charities, this process can occur both online and offline. The general concept is to combine the efforts of crowds of volunteers or part-time workers, where each one could contribute a small portion, which adds into a relatively large or significant result.</p>

  <div class="uses-ribbon abs">
    <svg width="358" height="38" viewBox="0 0 358 38"><polygon points="0,0 358,0 346,19 358,38 0,38 12,19" fill="#f7a237"/></svg>
    <span>Some uses of Crowdsourcing</span>
  </div>

  <section class="use-card abs" style="left:142px">
    <div class="use-photo" role="img" aria-label="Person in a suit with a glowing light bulb in place of the head" style="background:radial-gradient(circle at 50% 30%,#8a8a8a,#3a3a3a 70%,#222)"></div>
    <h2 class="use-title">Ideation</h2>
    <p class="use-text"><b>Here we have a short description of the Ideation use of crowdsourcing.</b> Lorem ipsum dolor sit amet, consectetur adipiscing elit. Vestibulum lectus ante, lacinia eu ultrices non, pellentesque at elit. Proin malesuada pellentesque libero a consectetur. Proin</p>
    <a href="#" class="learn-more">Learn More</a>
  </section>

  <section class="use-card abs" style="left:476px">
    <div class="use-photo" role="img" aria-label="Team of colleagues working together at a glass board" style="background:linear-gradient(135deg,#dfe8ee,#c9d6de 50%,#e8e2da)"></div>
    <h2 class="use-title">Crowdlabor</h2>
    <p class="use-text"><b>Here we have a short description of the Crowdlabor use of crowdsourcing.</b> Lorem ipsum dolor sit amet, consectetur adipiscing elit. Vestibulum lectus ante, lacinia eu ultrices non, pellentesque at elit. Proin malesuada pellentesque libero a consectetur.</p>
    <a href="#" class="learn-more">Learn More</a>
  </section>

  <section class="use-card abs" style="left:788px">
    <div class="use-photo" role="img" aria-label="Hands typing on a laptop keyboard" style="background:linear-gradient(160deg,#bfe3ee,#e6f2f6 55%,#b9c4cc)"></div>
    <h2 class="use-title">CrowdFeedback</h2>
    <p class="use-text"><b>Here we have a short description of the Crowdfeedback.</b> Lorem ipsum dolor sit amet, consectetur adipiscing elit. Vestibulum lectus ante, lacinia eu ultrices non, pellentesque at elit. Proin malesuada pellentesque libero a consectetur. Proin</p>
    <a href="#" class="learn-more">Learn More</a>
  </section>
</main>

<footer>
  <div class="footer-rule abs"></div>
  <p class="response-title footer-italic abs">Quick and Positive Response</p>
  <p class="response-phones abs">+00.555.010.2030 | +00.555.010.4090</p>
  <span class="footer-sep abs" style="left:389px"></span>
  <a class="footer-link footer-italic abs" style="left:413px">About Us</a>
  <span class="footer-sep abs" style="left:497px"></span>
  <a class="footer-link footer-italic abs" style="left:518px">What is Crowdsourcing?</a>
  <span class="footer-sep abs" style="left:706px"></span>
  <a class="footer-link footer-italic abs" style="left:728px">Solutions</a>
  <span class="footer-sep abs" style="left:816px"></span>
  <p class="newsletter-label footer-italic abs">Subscribe Newsletter</p>
  <div class="newsletter-field abs"><span class="newsletter-go"></span></div>
  <div class="footer-band abs"></div>
  <p class="copyright abs">Copyright 2013, All rights reserved.</p>
  <div class="like-box abs"><span class="like-btn">Like</span><span class="like-square"></span><span>10 people like this.</span></div>
</footer>

</body>
</html>
```